Web site design for Brivolt Software (www.brivoltsoftware-example.com)

Need the design as well as the html for the website. The brief is given in the attached file.
If possible, would like to use pencil sketches instead of images to give a unique look to the site.
Target Market(s)
small Software product companies
Industry/Entity Type
Software
Coding
Coded - Design and coding required
Number of Pages Required
5+ page

```html
<!DOCTYPE html>
<html lang="en">
<head>
<meta charset="utf-8">
<title>Brivolt Software — Typography</title>
<link rel="stylesheet" href="https://fonts.googleapis.com/css2?family=IBM+Plex+Mono:wght@400;600&family=Saira+Semi+Condensed:wght@500;600&display=swap">
<style>
  :root {
    --ink: #000000;
    --paper: #ffffff;
    --muted: #8a8a8a;
    --wave-tone: #1c1c1c;
    --heading-font: "Saira Semi Condensed", sans-serif;
    --mono-font: "IBM Plex Mono", monospace;
  }
  * { margin: 0; padding: 0; box-sizing: border-box; }
  html, body { width: 1200px; height: 1200px; overflow: hidden; background: var(--ink); }
  .canvas { position: relative; width: 1200px; height: 1200px; background: var(--ink); color: var(--paper); overflow: hidden; }
  .wave-field {
    position: absolute; inset: 0;
    background: radial-gradient(ellipse 90% 55% at 55% 12%, var(--wave-tone) 0%, #0b0b0b 55%, var(--ink) 80%);
  }
  .block { position: absolute; left: 230px; }
  .brand {
    position: absolute; left: 230px; top: 100px;
    font-family: var(--heading-font); font-weight: 600; font-size: 22px;
    letter-spacing: 9px; line-height: 30px; color: var(--paper);
  }
  .project-tag {
    position: absolute; right: 230px; top: 103px;
    font-family: var(--mono-font); font-size: 17px; line-height: 24px; color: var(--paper);
  }
  .section-title {
    top: 222px; font-family: var(--heading-font); font-weight: 600;
    font-size: 39px; line-height: 48px;
  }
  .intro {
    top: 284px; width: 720px; font-family: var(--mono-font);
    font-size: 17px; line-height: 22px;
  }
  .label {
    font-family: var(--mono-font); font-size: 16px; line-height: 20px; color: var(--muted);
  }
  .label-headings { top: 427px; }
  .sample-heading { top: 446px; font-family: var(--heading-font); font-weight: 600; font-size: 88px; line-height: 96px; }
  .label-text { top: 558px; }
  .sample-text { top: 580px; font-family: var(--heading-font); font-weight: 600; font-size: 27px; line-height: 34px; }
  .label-spans { top: 645px; }
  .sample-span { top: 667px; font-family: var(--mono-font); font-size: 27px; line-height: 34px; letter-spacing: 1px; }
  .divider { position: absolute; left: 230px; top: 747px; width: 740px; height: 4px; background: var(--paper); }
  .label-example { left: 227px; top: 770px; }
  .hero-title {
    top: 796px; left: 226px; font-family: var(--heading-font); font-weight: 600;
    font-size: 104px; line-height: 90px; letter-spacing: -1px;
  }
  .hero-lead {
    top: 1005px; font-family: var(--heading-font); font-weight: 600;
    font-size: 19px; line-height: 26px;
  }
  .hero-link {
    top: 1082px; font-family: var(--mono-font); font-weight: 600;
    font-size: 19px; line-height: 26px; letter-spacing: 1px;
  }
</style>
</head>
<body>
<main class="canvas">
  <div class="wave-field" role="img" aria-label="Faint flowing line pattern across the dark background"></div>

  <header>
    <div class="brand">BRIVOLT</div>
    <div class="project-tag">web design project</div>
  </header>

  <h1 class="block section-title">Cross-humanist typography</h1>
  <p class="block intro">We’ve used a combination of “Kalvera”, a cross of humanist and geometric, and “Mansard Mono”, a monolined grotesque based on a constructed principle to achieve an industrial flavour with a minimum of details and optical corrections</p>

  <span class="block label label-headings">Headings</span>
  <div class="block sample-heading">Kalvera</div>

  <span class="block label label-text">Text</span>
  <div class="block sample-text">Kalvera</div>

  <span class="block label label-spans">Spans</span>
  <div class="block sample-span">Mansard mono</div>

  <div class="divider"></div>

  <span class="block label label-example">Example</span>
  <h2 class="block hero-title">Driven by<br>architecture</h2>
  <p class="block hero-lead">Seasoned programmers who infuse rigor and<br>design into solid engineering in software</p>
  <a class="block hero-link">› who are we?</a>
</main>
</body>
</html>
```